Flyer Design Project

We need a flyer and teaser image designed for a March promotional campaign. We have a previous design that just needs a little refresh.
Flyer: the content of the flyer is mostly the same as the pdf you'll see on this link (http://www.quillbrookmedia.com/Digest_Pricing.pdf).
Here are the changes: change June to March, change 2011 to 2012, and remove the address of the bottom. I want the color scheme to be consistent with images I attached called "2011 teaser". I need a pdf file.
Teaser Image: the content of the teaser image is the same as "2011 teaser" image I have attached. All that needs to be changed is the month from "June" to "March". I need this to be a .jpg file that's 600x600 pixels.
Please let me know if you have any questions.
Thanks

```html
<!DOCTYPE html>
<html lang="en">
<head>
<meta charset="utf-8">
<title>Digest Pricing – March 2012</title>
<link rel="stylesheet" href="https://fonts.googleapis.com/css2?family=Open+Sans:ital,wght@0,400;0,600;1,400;1,700&family=Cabin+Condensed:wght@700&family=Amaranth:ital,wght@1,400&family=Lora:ital,wght@1,700&display=swap">
<style>
  :root {
    --backdrop: #e4e4e4;
    --border-teal: #3f6f78;
    --frame-brown: #7a4a26;
    --paper: #f8f1e0;
    --paper-glow: #fffaf0;
    --ink-teal: #2f6b7a;
    --title-teal: #3f7c8e;
    --tag-orange: #c9742f;
    --tag-orange-dark: #a85a22;
    --bar-orange: #eda235;
    --bar-orange-light: #f6bd55;
    --bar-teal: #5d9dac;
    --heading-brown: #6b3a1e;
    --row-ink: #2d2d2d;
    --accent-orange: #e08a2a;
    --white: #ffffff;
  }
  * { box-sizing: border-box; margin: 0; padding: 0; }
  html, body { width: 1200px; height: 746px; overflow: hidden; background: var(--backdrop); }
  .stage { position: relative; width: 1200px; height: 746px; overflow: hidden; }

  .flyer {
    position: absolute; left: 240px; top: -20px; width: 730px; height: 800px;
    background: var(--border-teal);
  }
  .flyer__paper {
    position: absolute; left: 34px; right: 34px; top: 0; bottom: 0;
    background: radial-gradient(ellipse 60% 45% at 50% 62%, var(--paper-glow) 0%, var(--paper) 70%);
    border-left: 3px solid var(--frame-brown);
    border-right: 3px solid var(--frame-brown);
    box-shadow: inset 5px 0 0 var(--paper), inset -5px 0 0 var(--paper);
  }

  .calendar-tag {
    position: absolute; left: 84px; top: 94px; width: 228px; height: 268px;
    background: linear-gradient(180deg, var(--tag-orange) 0%, var(--tag-orange-dark) 100%);
    box-shadow: 2px 4px 6px rgba(80, 40, 10, .35);
  }
  .calendar-tag__month {
    position: absolute; left: 0; right: 0; top: 12px; text-align: center;
    font: italic 700 26px "Lora", Georgia, serif; color: var(--white);
    border-bottom: 1px solid rgba(255,255,255,.5); margin: 0 18px; padding-bottom: 6px;
  }
  .calendar-tag__grid {
    position: absolute; left: 18px; top: 60px; width: 196px;
    display: grid; grid-template-columns: repeat(7, 1fr); grid-auto-rows: 29px;
    border-top: 1px solid rgba(255,255,255,.75); border-left: 1px solid rgba(255,255,255,.75);
  }
  .calendar-tag__grid span {
    border-right: 1px solid rgba(255,255,255,.75); border-bottom: 1px solid rgba(255,255,255,.75);
    font: italic 700 13px "Open Sans", Arial, sans-serif; color: var(--white);
    display: flex; align-items: center; justify-content: center;
  }
  .calendar-tag__fold {
    position: absolute; left: 0; right: 0; bottom: 0; height: 18px;
    background: linear-gradient(180deg, rgba(0,0,0,0) 0%, rgba(90,40,10,.35) 100%);
  }

  .offer-copy {
    position: absolute; left: 344px; top: 74px; width: 310px;
    font: 400 14px/18.6px "Open Sans", Arial, sans-serif; color: var(--ink-teal);
  }
  .offer-copy p + p { margin-top: 18px; }

  .pricing-title {
    position: absolute; left: 0; right: 0; top: 400px; text-align: center;
    font: 700 80px/1 "Cabin Condensed", "Arial Narrow", sans-serif; color: var(--title-teal);
    letter-spacing: 1px; text-shadow: 3px 3px 0 rgba(60, 90, 100, .25);
  }

  .price-table { position: absolute; left: 88px; top: 506px; width: 555px; }
  .price-table__heads {
    height: 34px; display: flex;
    background: linear-gradient(180deg, var(--bar-orange-light), var(--bar-orange));
  }
  .price-table__heads h2 {
    flex: 1; padding-left: 88px;
    font: italic 400 26px/34px "Amaranth", Georgia, serif; color: var(--heading-brown);
  }
  .price-table__labels {
    height: 27px; margin-top: 4px; display: flex; background: var(--bar-teal);
    font: italic 400 15px/27px "Open Sans", Arial, sans-serif; color: var(--white);
  }
  .price-table__labels span { width: 138.75px; padding-left: 20px; }
  .price-table__labels span:nth-child(even) { padding-left: 64px; }
  .price-table__body { display: flex; margin-top: 9px; }
  .price-table__col { flex: 1; padding-left: 18px; }
  .price-row {
    display: flex; height: 28.5px; width: 210px;
    font: italic 400 19px/28.5px "Open Sans", Arial, sans-serif; color: var(--row-ink);
  }
  .price-row__dots { flex: 1; overflow: hidden; white-space: nowrap; }
  .price-row__dots::before { content: "........................................"; }

  .contact-line {
    position: absolute; left: 0; right: 0; top: 738px; text-align: center;
    font: 400 15px "Open Sans", Arial, sans-serif; color: var(--ink-teal);
  }
  .contact-line i { font-style: normal; color: var(--accent-orange); padding: 0 4px; }
</style>
</head>
<body>
<main class="stage">
  <section class="flyer">
    <div class="flyer__paper"></div>

    <div class="calendar-tag">
      <div class="calendar-tag__month">March 2012</div>
      <div class="calendar-tag__grid">
        <span></span><span></span><span></span><span></span><span>1</span><span>2</span><span>3</span>
        <span>4</span><span>5</span><span>6</span><span>7</span><span>8</span><span>9</span><span>10</span>
        <span>11</span><span>12</span><span>13</span><span>14</span><span>15</span><span>16</span><span>17</span>
        <span>18</span><span>19</span><span>20</span><span>21</span><span>22</span><span>23</span><span>24</span>
        <span>25</span><span>26</span><span>27</span><span>28</span><span>29</span><span>30</span><span>31</span>
      </div>
      <div class="calendar-tag__fold"></div>
    </div>

    <div class="offer-copy">
      <p>Submit your art and order by 5:00 pm EST any business day in March to take advantage of this special pricing.</p>
      <p>Each 16 or 32-page digest includes 70# gloss paper throughout, bleeds and saddle-stitching.</p>
      <p>Your directory will be delivered within 12 business days. Note: Although your order may deliver sooner, we cannot accept early delivery requests.</p>
    </div>

    <h1 class="pricing-title">PRICING</h1>

    <div class="price-table">
      <div class="price-table__heads"><h2>16 Page</h2><h2>32 Page</h2></div>
      <div class="price-table__labels">
        <span>Quantity</span><span>Price</span><span>Quantity</span><span>Price</span>
      </div>
      <div class="price-table__body">
        <div class="price-table__col">
          <div class="price-row"><span>5,000</span><span class="price-row__dots"></span><span>$1,164.10</span></div>
          <div class="price-row"><span>10,000</span><span class="price-row__dots"></span><span>$1,446.40</span></div>
          <div class="price-row"><span>15,000</span><span class="price-row__dots"></span><span>$1,803.41</span></div>
          <div class="price-row"><span>20,000</span><span class="price-row__dots"></span><span>$2,148.79</span></div>
        </div>
        <div class="price-table__col">
          <div class="price-row"><span>5,000</span><span class="price-row__dots"></span><span>$1,999.52</span></div>
          <div class="price-row"><span>10,000</span><span class="price-row__dots"></span><span>$2,529.50</span></div>
          <div class="price-row"><span>15,000</span><span class="price-row__dots"></span><span>$3,173.53</span></div>
          <div class="price-row"><span>20,000</span><span class="price-row__dots"></span><span>$3,797.09</span></div>
        </div>
      </div>
    </div>

    <p class="contact-line">800-555-0142<i>/</i>317-555-0186<i>/</i>f 419-555-0173<i>/</i>www.quillbrookmedia.com</p>
  </section>
</main>
</body>
</html>
```